Business cards, stationary & real estate signs
LT&R Design
Business cards, stationary & real estate signs -
Creative Brief
Bright & Fun-filled
Joan V. Marsh
Broker, Realtor, CSP
4821 Tindall Lane, Suite 118 Maple Ridge, NC 27001
joan@gretaholmvale.example
www.joanmarsh-homes.example
In addition to business card and stationary we would also like a design for our real estate signs using the colors on our logo. The signs will be mounted to posts and will be 30x24in

```html
<!DOCTYPE html>
<html lang="en">
<head>
<meta charset="utf-8">
<title>LT&amp;R Design – Business Cards</title>
<link href="https://fonts.googleapis.com/css2?family=Open+Sans:wght@400;600;700&display=swap" rel="stylesheet">
<style>
  :root {
    --stage: #e9ebee;
    --card-white: #ffffff;
    --brand-blue: #1f57a6;
    --brand-blue-light: #3a86cf;
    --brand-blue-deep: #1a4a92;
    --brand-teal: #1e7dba;
    --brand-green: #9cc83a;
    --ink: #2b2f36;
    --shadow: rgba(20, 30, 50, 0.22);
  }
  * { box-sizing: border-box; margin: 0; padding: 0; }
  html, body {
    width: 1200px; height: 804px; overflow: hidden;
    background: var(--stage);
    font-family: "Open Sans", Arial, sans-serif;
  }
  .canvas { position: relative; width: 1200px; height: 804px; }

  .card {
    position: absolute;
    height: 271px;
    border-radius: 16px;
    overflow: hidden;
    box-shadow: 0 8px 22px var(--shadow);
    background: var(--card-white);
  }
  .card--front { left: 372px; top: 91px; width: 470px; }
  .card--back-blue { left: 96px; top: 396px; width: 530px; background: var(--brand-blue-deep); }
  .card--back-white { left: 660px; top: 396px; width: 530px; }

  .wordmark {
    position: absolute;
    font-weight: 700;
    letter-spacing: 0.5px;
    white-space: nowrap;
    line-height: 1;
  }

  /* Front card */
  .front-band {
    position: absolute; left: 0; top: 0; width: 100%; height: 106px;
    background: linear-gradient(180deg, var(--brand-blue-light) 0%, var(--brand-blue) 100%);
  }
  .front-rule {
    position: absolute; left: 0; top: 106px; width: 100%; height: 3px;
    background: var(--brand-green);
  }
  .front-name {
    position: absolute; left: 20px; top: 14px; color: #fff;
    font-size: 15px; font-weight: 700; line-height: 1.2;
  }
  .front-title {
    position: absolute; left: 20px; top: 36px; color: #fff;
    font-size: 12px; font-weight: 400; line-height: 1.2;
  }
  .card--front .wordmark {
    right: 22px; top: 124px; font-size: 30px; color: var(--brand-teal);
  }
  .front-contact {
    position: absolute; left: 20px; top: 160px;
    font-size: 11px; line-height: 15px; color: var(--ink);
    list-style: none;
  }
  .front-contact .label { color: var(--brand-blue); font-weight: 700; display: inline-block; width: 14px; }
  .front-contact .address { margin-bottom: 6px; }

  /* Blue back */
  .card--back-blue .wordmark {
    left: 0; right: 0; text-align: center; top: 116px;
    font-size: 40px; color: #fff;
  }
  .blue-rule {
    position: absolute; left: 0; bottom: 36px; width: 100%; height: 3px;
    background: var(--brand-green);
  }
  .blue-footer {
    position: absolute; left: 0; bottom: 0; width: 100%; height: 36px;
    background: var(--card-white);
    display: flex; align-items: center; justify-content: center;
    font-size: 12px; font-weight: 700; letter-spacing: 1px; color: var(--brand-blue);
  }

  /* White back */
  .card--back-white .wordmark {
    left: 0; right: 0; text-align: center; top: 116px;
    font-size: 40px; color: var(--brand-teal);
  }
  .white-rule {
    position: absolute; left: 0; bottom: 36px; width: 100%; height: 3px;
    background: var(--brand-green);
  }
  .white-footer {
    position: absolute; left: 0; bottom: 0; width: 100%; height: 36px;
    display: flex; align-items: center; justify-content: center;
    font-size: 12px; font-weight: 700; letter-spacing: 1px; color: var(--brand-blue);
  }
</style>
</head>
<body>
<main class="canvas">

  <section class="card card--front" aria-label="Business card front">
    <div class="front-band"></div>
    <div class="front-rule"></div>
    <h1 class="front-name">Joan V. Marsh</h1>
    <p class="front-title">Broker, Realtor, CSP</p>
    <div class="wordmark">LT&amp;R Design</div>
    <ul class="front-contact">
      <li class="address">4821 Tindall Lane, Suite 118<br>Maple Ridge, NC 27001</li>
      <li><span class="label">P</span>: 919-555-0142</li>
      <li><span class="label">F</span>: 919-555-0187</li>
      <li><span class="label">E</span>: joan@gretaholmvale.example</li>
      <li><span class="label">W</span>: www.joanmarsh-homes.example</li>
    </ul>
  </section>

  <section class="card card--back-blue" aria-label="Business card back, blue">
    <div class="wordmark">LT&amp;R Design</div>
    <div class="blue-rule"></div>
    <div class="blue-footer">www.joanmarsh-homes.example</div>
  </section>

  <section class="card card--back-white" aria-label="Business card back, white">
    <div class="wordmark">LT&amp;R Design</div>
    <div class="white-rule"></div>
    <div class="white-footer">www.joanmarsh-homes.example</div>
  </section>

</main>
</body>
</html>
```